LA's Newest HEMP Facial Oil and Body Oil Packaging Project

We need a packaging concept for a Hemp based facial oil and body oil. We need label design for the bottle and carton graphics. I am attaching a few reference photos. The target demographic is women between 17-35 year old. Products need to be able to stand out in crowded stores with clear calls to action.
1oz Dropper Bottle with Unit Carton - Hemp Facial Oil
4oz PET Bottle with Unit Carton - Hemp + Rose Facial Oil

```html
<!DOCTYPE html>
<html lang="en">
<head>
<meta charset="utf-8">
<title>Hemp Facial Oil and Body Oil Packaging</title>
<link href="https://fonts.googleapis.com/css2?family=Bitter:wght@500&family=Montserrat:wght@400;500&display=swap" rel="stylesheet">
<style>
  :root {
    --red: #e31c48;
    --lime: #cfd927;
    --green-a: #9fc93c;
    --green-b: #7ebf45;
    --white: #ffffff;
    --ink: #1a1a1a;
    --bg: #f3f3f3;
    --serif: "Bitter", Georgia, serif;
    --sans: "Montserrat", Arial, sans-serif;
  }
  * { box-sizing: border-box; margin: 0; padding: 0; }
  html, body { width: 1200px; height: 900px; overflow: hidden; background: var(--bg); }
  .canvas { position: relative; width: 1200px; height: 900px; }

  .panel { position: absolute; overflow: hidden; }
  .label { background: var(--white); box-shadow: 0 0 0 1px #e2e2e2; }
  .carton { background: var(--red); }
  .carton-top { position: absolute; left: 0; top: 0; width: 100%; background: var(--lime); }

  .swatch { position: absolute; display: flex; }
  .swatch span { display: block; height: 100%; }

  .leaf-art { position: absolute; }

  .name { font-family: var(--serif); font-weight: 500; line-height: 1; position: absolute; }
  .variant { font-family: var(--sans); font-weight: 400; line-height: 1; position: absolute; letter-spacing: 0.02em; }
  .claim { font-family: var(--sans); font-weight: 500; position: absolute; text-align: center; line-height: 1.15; }
  .size-note { font-family: var(--sans); position: absolute; text-align: center; line-height: 1.2; text-transform: uppercase; }
  .drop { position: absolute; }

  .vertical { writing-mode: vertical-rl; transform: rotate(180deg); white-space: nowrap; }

  /* facial label */
  .facial-label { left: 140px; top: 430px; width: 162px; height: 250px; }
  /* facial carton */
  .facial-carton { left: 367px; top: 218px; width: 190px; height: 477px; }
  /* body label */
  .body-label { left: 694px; top: 330px; width: 128px; height: 360px; }
  /* body carton */
  .body-carton { left: 903px; top: 218px; width: 164px; height: 477px; }
</style>
</head>
<body>
<main class="canvas">

  <!-- Facial oil bottle label -->
  <section class="panel label facial-label" aria-label="Hemp Facial Oil bottle label">
    <div class="swatch" style="left:0;top:25px;width:54px;height:40px;">
      <span style="width:32px;background:var(--red)"></span>
      <span style="width:22px;background:var(--lime)"></span>
    </div>
    <div class="leaf-art" role="img" aria-label="Line drawing of hemp leaves" style="right:0;top:0;width:95px;height:110px;background:radial-gradient(circle at 80% 25%, rgba(207,217,39,.45), rgba(207,217,39,0) 70%);"></div>
    <div class="name" style="left:24px;top:116px;font-size:40px;color:var(--lime);">Hemp</div>
    <div class="variant" style="left:25px;top:158px;font-size:16px;color:var(--ink);">FACIAL OIL</div>
    <div class="leaf-art" role="img" aria-label="Line drawing of a leaf sprig" style="left:0;top:195px;width:50px;height:50px;background:radial-gradient(circle at 40% 50%, rgba(207,217,39,.45), rgba(207,217,39,0) 70%);"></div>
    <div class="claim" style="left:45px;top:212px;width:80px;font-size:8px;color:var(--ink);">With Hemp oil<br>and Rose</div>
    <svg class="drop" style="left:128px;top:195px;" width="26" height="34" viewBox="0 0 26 34" aria-hidden="true">
      <path d="M13 1 C13 1 2 15 2 22 a11 11 0 0 0 22 0 C24 15 13 1 13 1Z" fill="var(--red)"/>
      <text x="11" y="27" font-family="Montserrat, sans-serif" font-size="11" font-weight="500" fill="#fff" text-anchor="middle">1</text>
      <text x="18" y="23" font-family="Montserrat, sans-serif" font-size="5" fill="#fff" text-anchor="middle">oz</text>
    </svg>
    <div class="size-note" style="left:120px;top:231px;width:42px;font-size:4px;color:var(--ink);">Dropper<br>Bottle</div>
  </section>

  <!-- Facial oil carton -->
  <section class="panel carton facial-carton" aria-label="Hemp Facial Oil carton">
    <div class="carton-top" style="height:213px;"></div>
    <div class="swatch" style="left:0;top:67px;width:68px;height:43px;">
      <span style="width:46px;background:var(--green-a)"></span>
      <span style="width:22px;background:var(--green-b)"></span>
    </div>
    <div class="leaf-art" role="img" aria-label="White line drawing of hemp leaves" style="right:0;top:0;width:130px;height:155px;background:radial-gradient(circle at 75% 35%, rgba(255,255,255,.45), rgba(255,255,255,0) 70%);"></div>
    <div class="name" style="left:18px;top:230px;font-size:54px;color:var(--white);">Hemp</div>
    <div class="variant" style="left:21px;top:287px;font-size:20px;color:var(--white);">FACIAL OIL</div>
    <div class="claim" style="left:0;top:355px;width:100%;font-size:10px;color:var(--white);">With Hemp oil<br>and Rose</div>
    <div class="leaf-art" role="img" aria-label="White line drawing of a leaf sprig" style="left:4px;top:400px;width:70px;height:72px;background:radial-gradient(circle at 45% 50%, rgba(255,255,255,.4), rgba(255,255,255,0) 70%);"></div>
    <svg class="drop" style="left:138px;top:402px;" width="34" height="44" viewBox="0 0 34 44" aria-hidden="true">
      <path d="M17 1 C17 1 2 20 2 29 a15 15 0 0 0 30 0 C32 20 17 1 17 1Z" fill="#fff"/>
      <text x="15" y="36" font-family="Montserrat, sans-serif" font-size="15" font-weight="500" fill="var(--lime)" text-anchor="middle">1</text>
      <text x="24" y="30" font-family="Montserrat, sans-serif" font-size="6" fill="var(--lime)" text-anchor="middle">oz</text>
    </svg>
    <div class="size-note" style="left:128px;top:451px;width:54px;font-size:6px;color:var(--white);">Dropper<br>Bottle</div>
  </section>

  <!-- Body oil bottle label -->
  <section class="panel label body-label" aria-label="Hemp Body Oil bottle label">
    <div class="swatch" style="left:0;top:50px;width:48px;height:32px;">
      <span style="width:32px;background:var(--red)"></span>
      <span style="width:16px;background:var(--lime)"></span>
    </div>
    <div class="leaf-art" role="img" aria-label="Line drawing of hemp leaves" style="right:0;top:10px;width:80px;height:105px;background:radial-gradient(circle at 65% 40%, rgba(207,217,39,.45), rgba(207,217,39,0) 70%);"></div>
    <div class="name vertical" style="left:28px;top:112px;font-size:44px;color:var(--lime);">Hemp</div>
    <div class="variant vertical" style="left:74px;top:158px;font-size:18px;color:var(--ink);">BODY OIL</div>
    <svg class="drop" style="left:50px;top:262px;" width="26" height="34" viewBox="0 0 26 34" aria-hidden="true">
      <path d="M13 1 C13 1 2 15 2 22 a11 11 0 0 0 22 0 C24 15 13 1 13 1Z" fill="var(--red)"/>
      <text x="11" y="27" font-family="Montserrat, sans-serif" font-size="11" font-weight="500" fill="#fff" text-anchor="middle">1</text>
      <text x="18" y="23" font-family="Montserrat, sans-serif" font-size="5" fill="#fff" text-anchor="middle">oz</text>
    </svg>
    <div class="size-note" style="left:30px;top:300px;width:66px;font-size:4px;color:var(--ink);">Dropper Bottle</div>
    <div class="leaf-art" role="img" aria-label="Line drawing of a leaf sprig" style="left:0;top:302px;width:44px;height:44px;background:radial-gradient(circle at 40% 50%, rgba(207,217,39,.45), rgba(207,217,39,0) 70%);"></div>
    <div class="claim" style="left:30px;top:328px;width:76px;font-size:8px;color:var(--ink);">With Hemp oil<br>and Rose</div>
  </section>

  <!-- Body oil carton -->
  <section class="panel carton body-carton" aria-label="Hemp Body Oil carton">
    <div class="carton-top" style="height:205px;"></div>
    <div class="swatch" style="left:0;top:65px;width:60px;height:38px;">
      <span style="width:41px;background:var(--green-a)"></span>
      <span style="width:19px;background:var(--green-b)"></span>
    </div>
    <div class="leaf-art" role="img" aria-label="White line drawing of hemp leaves" style="right:0;top:0;width:115px;height:140px;background:radial-gradient(circle at 70% 40%, rgba(255,255,255,.45), rgba(255,255,255,0) 70%);"></div>
    <div class="name vertical" style="left:42px;top:150px;font-size:64px;color:var(--white);">Hemp</div>
    <div class="variant vertical" style="left:112px;top:214px;font-size:21px;color:var(--white);">BODY OIL</div>
    <svg class="drop" style="left:65px;top:352px;" width="34" height="44" viewBox="0 0 34 44" aria-hidden="true">
      <path d="M17 1 C17 1 2 20 2 29 a15 15 0 0 0 30 0 C32 20 17 1 17 1Z" fill="#fff"/>
      <text x="15" y="36" font-family="Montserrat, sans-serif" font-size="15" font-weight="500" fill="var(--lime)" text-anchor="middle">1</text>
      <text x="24" y="30" font-family="Montserrat, sans-serif" font-size="6" fill="var(--lime)" text-anchor="middle">oz</text>
    </svg>
    <div class="size-note" style="left:0;top:412px;width:100%;font-size:6px;color:var(--white);">Dropper<br>Bottle</div>
    <div class="claim" style="left:0;top:437px;width:100%;font-size:10px;color:var(--white);">With Hemp oil<br>and Rose</div>
  </section>

</main>
</body>
</html>
```